Zeitloses Etiketten-Design für Zirbenlikör gesucht
Zielgruppe
Wir sind ein Betrieb der kunsthandwerkliche Gegenstände aus Holz herstellt, vor allem aus Zirbe. Da wir seit 3 Jahren auch Zirbenlikör herstellen, suchen wir für diese ein neues Etikett.
Aufgabenstellung
Zirbelikör wird aus den Zapfen der Zirbe hergestellt. Auf der Zirbe wachsen die Zapfen das erste mal nach ca. 20 Jahren. Sie wächst in ca. 1500 - 2500m Seehöhe und ist sehr wiederstandsfähig. Die Typische Farbe des Likörs ist Dunkelrot.
Ein paar dieser Dinge sollte man dem Etikett wieder finden. Vielleicht auch Berge im Hintergrund...
Klassisch, Zeitlos, Edel, vl. auch verspielt ( vor allem das Wort Zirbe), Wiedererkennungswert und meinen Namen: KESTLER
Die Adresse kann gerne auch seitlich stehen.
Das alte Etikett habe ich selbst gemacht, es ist 6,5x10,5 cm. Fürs erste nicht so schlecht, zum expandieren eine Katastrophe.

```html
<!DOCTYPE html>
<html lang="de">
<head>
<meta charset="utf-8">
<title>Zirben Likör – Etiketten</title>
<link rel="stylesheet" href="https://fonts.googleapis.com/css2?family=Amatic+SC:wght@400;700&family=Saira+Condensed:wght@300;400;700&display=swap">
<style>
  :root {
    --page: #ffffff;
    --label-white: #ffffff;
    --wine: #6b1619;
    --wine-soft: #8a3a3c;
    --ink: #1c1416;
    --cream: #ffffff;
  }
  * { box-sizing: border-box; margin: 0; padding: 0; }
  html, body {
    width: 1200px; height: 2400px; overflow: hidden;
    background: var(--page);
  }
  .canvas { position: relative; width: 1200px; height: 2400px; }
  .label {
    position: absolute; left: 290px; width: 620px; height: 1003px;
    background: var(--label-white);
    box-shadow: 0 3px 8px rgba(0,0,0,0.25);
    overflow: hidden; text-align: center;
  }
  .label--rustic { top: 120px; font-family: "Amatic SC", sans-serif; }
  .label--modern { top: 1277px; font-family: "Saira Condensed", sans-serif; }

  .emblem {
    position: absolute; left: 140px; top: 60px; width: 340px; height: 142px;
    background: radial-gradient(ellipse at 50% 100%, var(--wine) 0 28%, rgba(107,22,25,0.35) 29% 70%, transparent 71%);
  }
  .forest {
    position: absolute; left: 0; top: 380px; width: 620px; height: 300px;
    background: linear-gradient(to bottom, rgba(107,22,25,0.15) 0%, rgba(107,22,25,0.7) 45%, var(--wine) 100%);
  }
  .band {
    position: absolute; left: 0; top: 678px; width: 620px; height: 325px;
    background: var(--wine);
  }
  .text { position: absolute; left: 0; width: 620px; line-height: 1; }

  /* rustic variant */
  .label--rustic .title { top: 208px; font-size: 94px; font-weight: 700; color: var(--ink); letter-spacing: 1px; }
  .label--rustic .subtitle { top: 292px; font-size: 56px; font-weight: 700; color: var(--wine); letter-spacing: 2px; }
  .label--rustic .abv { top: 345px; font-size: 32px; color: var(--ink); }
  .label--rustic .maker { top: 700px; font-size: 56px; color: var(--cream); }
  .label--rustic .street { top: 764px; font-size: 62px; color: var(--cream); letter-spacing: 1px; }
  .label--rustic .town { top: 832px; font-size: 62px; color: var(--cream); letter-spacing: 1px; }
  .label--rustic .volume { top: 935px; font-size: 40px; color: var(--cream); }

  /* modern variant */
  .label--modern .title { top: 222px; font-size: 80px; font-weight: 700; color: var(--ink); letter-spacing: 3px; }
  .label--modern .subtitle { top: 302px; font-size: 48px; font-weight: 700; color: var(--wine); letter-spacing: 2px; }
  .label--modern .abv { top: 357px; font-size: 28px; font-weight: 700; color: var(--ink); letter-spacing: 1px; }
  .label--modern .maker { top: 705px; font-size: 46px; font-weight: 700; color: var(--cream); letter-spacing: 2px; }
  .label--modern .street { top: 770px; font-size: 48px; font-weight: 300; color: var(--cream); letter-spacing: 3px; }
  .label--modern .town { top: 828px; font-size: 48px; font-weight: 300; color: var(--cream); letter-spacing: 3px; }
  .label--modern .volume { top: 935px; font-size: 36px; font-weight: 700; color: var(--cream); }
</style>
</head>
<body>
<main class="canvas">
  <section class="label label--rustic">
    <div class="emblem" role="img" aria-label="Drei Zirben vor einem Strahlenkranz"></div>
    <h1 class="text title">Zirben Likör</h1>
    <p class="text subtitle">Hausgemachter</p>
    <p class="text abv">29,7 % vol</p>
    <div class="forest" role="img" aria-label="Silhouette eines Zirbenwaldes"></div>
    <div class="band"></div>
    <p class="text maker">Thomas Kestler</p>
    <p class="text street">Lindenhofgasse 14</p>
    <p class="text town">3482 Waldberg</p>
    <p class="text volume">500ml</p>
  </section>

  <section class="label label--modern">
    <div class="emblem" role="img" aria-label="Drei Zirben vor einem Strahlenkranz"></div>
    <h1 class="text title">ZIRBEN LIKÖR</h1>
    <p class="text subtitle">HAUSGEMACHTER</p>
    <p class="text abv">29,7 % VOL</p>
    <div class="forest" role="img" aria-label="Silhouette eines Zirbenwaldes"></div>
    <div class="band"></div>
    <p class="text maker">THOMAS KESTLER</p>
    <p class="text street">LINDENHOFGASSE 14</p>
    <p class="text town">3482 WALDBERG</p>
    <p class="text volume">500ML</p>
  </section>
</main>
</body>
</html>
```